New Zealand Luggage Importer Needs Business Cards

We need professional, creative and fashionable business cards created.
We are based in New Zealand and import and distribute high-end, quality, fashionable and durable luggage.
We pride ourselves on selling the very best quality luggage, second only to 1 brand (which we won't mention here)...we use the same manufacturer. However, our prices are much more reasonable.
Business
Sam Ortiz
027 481 2956
3/17 Kestrel Lane, Morrow Flats, Auckland, 0614
PO Box 208354, North Shore, Auckland 0792
09-527-3061
sales@brindlecases.co.nz / www.brindlecases.co.nz

```html
<!DOCTYPE html>
<html lang="en">
<head>
<meta charset="utf-8">
<title>Brindle Cases – Business Card</title>
<link rel="stylesheet" href="https://fonts.googleapis.com/css2?family=Roboto:wght@300;400;500;700&display=swap">
<style>
  :root {
    --stage: #4b5672;
    --card-dark: #3b4153;
    --card-frame: #2e3342;
    --panel: #4c5266;
    --panel-line: #3a3f50;
    --teal: #8eaeb7;
    --logo-bar: #3a4054;
    --text-light: #ffffff;
    --text-teal: #9cc3c9;
    --rule: #5a6174;
    --red: #d9463b;
    --yellow: #e0a53b;
    --purple: #7c569d;
    --green: #3fae87;
    --accent-red: #d9503a;
  }
  * { box-sizing: border-box; margin: 0; padding: 0; }
  html, body { width: 1200px; height: 1200px; overflow: hidden; }
  body {
    background: var(--stage);
    font-family: "Roboto", Arial, sans-serif;
    position: relative;
  }
  .card {
    position: absolute;
    top: 250px;
    width: 400px;
    height: 700px;
    box-shadow: 0 18px 40px rgba(0,0,0,.35);
    overflow: hidden;
  }
  /* ---------- Front ---------- */
  .card-front { left: 170px; background: var(--card-dark); }
  .front-header {
    position: absolute; left: 0; top: 0; width: 100%; height: 230px;
    background: var(--teal);
  }
  .logo-bar {
    position: absolute; display: flex; align-items: center; justify-content: center;
    background: var(--logo-bar); color: var(--text-light);
    font-weight: 700; letter-spacing: 3px; text-transform: uppercase;
  }
  .front-header .logo-bar {
    left: 40px; top: 80px; width: 320px; height: 70px; font-size: 26px;
  }
  .front-tick {
    position: absolute; right: 34px; top: 250px; width: 4px; height: 34px;
    background: var(--text-light);
  }
  .info-row {
    position: absolute; left: 0; width: 100%; display: flex; align-items: center;
  }
  .info-row::after {
    content: ""; position: absolute; left: 110px; right: 30px; bottom: 0;
    height: 1px; background: var(--rule);
  }
  .info-row:last-child::after { display: none; }
  .tile {
    width: 92px; height: 100%; display: flex; align-items: center; justify-content: center;
    flex: none;
  }
  .tile svg { width: 32px; height: 32px; }
  .tile-person { background: transparent; }
  .tile-phone { background: var(--red); }
  .tile-mail { background: var(--yellow); }
  .tile-web { background: var(--purple); }
  .tile-home { background: var(--green); }
  .info-text {
    padding-left: 26px; color: var(--text-teal); font-size: 15px; line-height: 1.45;
    font-weight: 400;
  }
  .holder-name { color: var(--text-light); font-size: 24px; font-weight: 700; letter-spacing: .5px; }
  .holder-title { color: var(--text-teal); font-size: 14px; font-weight: 300; }
  .row-name { top: 230px; height: 100px; }
  .row-phone { top: 330px; height: 92px; }
  .row-mail { top: 422px; height: 92px; }
  .row-web { top: 514px; height: 92px; }
  .row-home { top: 606px; height: 94px; }
  .row-home .info-text { font-size: 13.5px; line-height: 1.35; }

  /* ---------- Back ---------- */
  .card-back { left: 630px; background: var(--card-frame); }
  .back-panel {
    position: absolute; left: 30px; top: 30px; right: 30px; bottom: 30px;
    background: var(--panel);
  }
  .panel-divider {
    position: absolute; left: 0; right: 0; height: 1px; background: var(--panel-line);
  }
  .divider-top { top: 213px; }
  .divider-bottom { top: 426px; }
  .accent-line {
    position: absolute; height: 4px; background: var(--accent-red);
  }
  .accent-top { top: 211px; right: 0; width: 120px; }
  .accent-bottom { top: 424px; left: 0; width: 120px; }
  .back-panel .logo-bar {
    left: 30px; right: 30px; top: 283px; height: 74px; font-size: 26px;
  }
</style>
</head>
<body>

<section class="card card-front" aria-label="Business card front">
  <div class="front-header">
    <div class="logo-bar">Brindle Cases</div>
  </div>
  <div class="front-tick"></div>

  <div class="info-rows">
    <div class="info-row row-name">
      <div class="tile tile-person">
        <svg viewBox="0 0 32 32" aria-hidden="true"><circle cx="16" cy="11" r="6" fill="#fff"/><path d="M5 29c0-7 5-11 11-11s11 4 11 11z" fill="#fff"/></svg>
      </div>
      <div class="info-text">
        <div class="holder-name">SAM ORTIZ</div>
        <div class="holder-title">Company Owner</div>
      </div>
    </div>

    <div class="info-row row-phone">
      <div class="tile tile-phone">
        <svg viewBox="0 0 32 32" aria-hidden="true"><path d="M9 4l5 6-3 3c2 4 4 6 8 8l3-3 6 5-3 5C15 28 4 17 4 7z" fill="#fff"/></svg>
      </div>
      <div class="info-text">027 481 2956<br>09-527-3061</div>
    </div>

    <div class="info-row row-mail">
      <div class="tile tile-mail">
        <svg viewBox="0 0 32 32" aria-hidden="true"><rect x="4" y="8" width="24" height="16" fill="#fff"/><path d="M4 8l12 10 12-10" fill="none" stroke="#e0a53b" stroke-width="2"/></svg>
      </div>
      <div class="info-text">sales@brindlecases.co.nz</div>
    </div>

    <div class="info-row row-web">
      <div class="tile tile-web">
        <svg viewBox="0 0 32 32" aria-hidden="true" fill="none" stroke="#fff" stroke-width="2"><circle cx="16" cy="16" r="12"/><ellipse cx="16" cy="16" rx="5" ry="12"/><path d="M4 16h24M6 10h20M6 22h20"/></svg>
      </div>
      <div class="info-text">www.brindlecases.co.nz</div>
    </div>

    <div class="info-row row-home">
      <div class="tile tile-home">
        <svg viewBox="0 0 32 32" aria-hidden="true"><path d="M16 5L3 17h5v10h6v-7h4v7h6V17h5z" fill="#fff"/></svg>
      </div>
      <div class="info-text">3/17 Kestrel Lane, Morrow Flats,<br>Auckland, 0614<br>PO Box 208354, North Shore,<br>Auckland 0792</div>
    </div>
  </div>
</section>

<section class="card card-back" aria-label="Business card back">
  <div class="back-panel">
    <div class="panel-divider divider-top"></div>
    <div class="panel-divider divider-bottom"></div>
    <div class="accent-line accent-top"></div>
    <div class="accent-line accent-bottom"></div>
    <div class="logo-bar">Brindle Cases</div>
  </div>
</section>

</body>
</html>
```